2-Sided Flyer for Printing - Quarvelent

We are looking for the most attractive and best quality flyer to serve as a handout to distribute as a printed document in fairs and conventions. We want one A4 sheet using two sides to display what is Quarvelent in an attractive and simple way.
• What is Quarvelent, what we do and benefits
o Type of challenges we solve
o Benefit for the companies
o Benefit for the solvers (engineers)
• How does it work
• Sample challenges
• Show our Community (skills, solvers pictures, etc)
The flyer should be developed according to our corporate colours (see landing page and logo)
The material we are uploading is the following:
• Power point with the introduction to Quarvelent
• Sample non professional flyers
• In addition you can use any material available through our web: www.quarvelent-example.com (landing page, blog, clients pages, ranking, etc.)

Target Market(s)

industrial companies and engineers

Industry/Entity Type

Engineering

Requirements
Must have
• A single flyer to be used for companies (clients) and engineers (solvers)
• overall flyer creative design
• clear and clean messages
• contain what is Quarvelent, how it works, community and sample challenges
• social networks info
• corporate pallet
Nice to have
• attractive funnel design to show how to move from a challenge to unique solutions
• attractive way to show the crowd using real solvers pictures
• Not all the background should be coloured (combination of white and corporate colours)
Should not have
• Copy and paste of the provided information and pictures
• High density content
• We do not like the design of the file "Brochure OK final.pdf" and we are looking for a 2-sided flyer

```html
<!DOCTYPE html>
<html lang="en">
<head>
<meta charset="utf-8">
<title>Quarvelent Flyer – What Can You Expect From Us</title>
<link href="https://fonts.googleapis.com/css2?family=Poppins:wght@400;500;700&display=swap" rel="stylesheet">
<style>
  :root {
    --frame: #000000;
    --teal: #1aa89a;
    --orange: #e84e1b;
    --lime: #cdd500;
    --sky: #2ea8e0;
    --mist: #e7eff6;
    --mist-warm: #eef0e8;
    --slate: #3f6475;
    --white: #ffffff;
    --ink: #3a3a3a;
  }
  * { box-sizing: border-box; margin: 0; padding: 0; }
  html, body {
    width: 1150px;
    height: 1200px;
    overflow: hidden;
    background: var(--frame);
  }
  .flyer {
    position: relative;
    width: 1150px;
    height: 1200px;
    background: var(--frame);
    font-family: Arial, Helvetica, sans-serif;
  }
  .hero {
    position: absolute;
    left: 15px; top: 15px;
    width: 1118px; height: 337px;
    background: var(--teal);
    color: var(--white);
  }
  .hero-title {
    position: absolute;
    left: 48px; top: 20px;
    font-family: "Poppins", sans-serif;
    font-weight: 700;
    font-size: 45px;
    line-height: 55px;
    letter-spacing: 0.5px;
  }
  .hero-copy {
    position: absolute;
    left: 55px;
    width: 660px;
    font-size: 21px;
    line-height: 32px;
  }
  .hero-copy.first { top: 164px; }
  .hero-copy.second { top: 244px; }
  .brand-tile {
    position: absolute;
    left: 742px; top: 0;
    width: 355px; height: 254px;
    background: var(--white);
    border-radius: 0 0 12px 12px;
    display: flex;
    align-items: center;
    justify-content: center;
  }
  .brand-name {
    font-family: "Poppins", sans-serif;
    font-weight: 400;
    font-size: 54px;
    color: var(--ink);
    letter-spacing: 1px;
  }
  .promise-band {
    position: absolute;
    left: 15px; top: 352px;
    width: 1118px; height: 109px;
    background: var(--orange);
  }
  .promise-heading {
    position: absolute;
    left: 76px; top: 20px;
    font-family: "Poppins", sans-serif;
    font-weight: 700;
    font-size: 53px;
    line-height: 68px;
    color: var(--white);
  }
  .benefits {
    position: absolute;
    left: 15px; top: 461px;
    width: 1118px; height: 680px;
    overflow: hidden;
  }
  .benefits-backdrop {
    position: absolute;
    inset: 0;
    background: linear-gradient(135deg, var(--mist) 0%, var(--mist-warm) 45%, var(--mist) 75%, #f0e6e6 100%);
  }
  .benefit {
    position: absolute;
    width: 396px; height: 396px;
    border-radius: 50%;
    border: 6px solid var(--white);
    color: var(--white);
    text-align: center;
    display: flex;
    flex-direction: column;
    align-items: center;
    justify-content: center;
  }
  .benefit.lime { left: 82px; top: 252px; background: var(--lime); z-index: 1; }
  .benefit.orange { left: 366px; top: 20px; background: var(--orange); z-index: 2; }
  .benefit.sky { left: 658px; top: 243px; background: var(--sky); z-index: 3; }
  .benefit-title {
    font-family: "Poppins", sans-serif;
    font-weight: 500;
    font-size: 30px;
    line-height: 40px;
    margin-bottom: 12px;
  }
  .benefit-text {
    font-size: 22px;
    line-height: 35px;
  }
  .footer-bar {
    position: absolute;
    left: 15px; top: 1141px;
    width: 1118px; height: 41px;
    background: var(--slate);
  }
</style>
</head>
<body>
<main class="flyer">
  <header class="hero">
    <h1 class="hero-title">Turn Innovation into<br>Tangible Results</h1>
    <p class="hero-copy first">Subtext here Subtext here Subtext here Subtext hereSubtext here Subtext here Subtext here Subtext here</p>
    <p class="hero-copy second">Subtext here Subtext here Subtext here Subtext hereSubtext here Subtext here Subtext here Subtext here</p>
    <div class="brand-tile">
      <span class="brand-name">quarvelent</span>
    </div>
  </header>

  <section class="promise-band">
    <h2 class="promise-heading">WHAT CAN YOU EXPECT FROM US</h2>
  </section>

  <section class="benefits">
    <div class="benefits-backdrop" role="img" aria-label="Soft pastel background of scattered faint geometric tiles in teal, orange, lime and blue tones"></div>

    <article class="benefit lime">
      <h3 class="benefit-title">Title Points Here</h3>
      <p class="benefit-text">Subtext here Subtext here<br>Subtext here Subtext her-<br>eSubtext here Subtext here<br>Subtext here Subtext here</p>
    </article>

    <article class="benefit orange">
      <h3 class="benefit-title">Title Points Here</h3>
      <p class="benefit-text">Subtext here Subtext here<br>Subtext here Subtext her-<br>eSubtext here Subtext here<br>Subtext here Subtext here</p>
    </article>

    <article class="benefit sky">
      <h3 class="benefit-title">Title Points Here</h3>
      <p class="benefit-text">Subtext here Subtext here<br>Subtext here Subtext her-<br>eSubtext here Subtext here<br>Subtext here Subtext here</p>
    </article>
  </section>

  <footer class="footer-bar"></footer>
</main>
</body>
</html>
```